Tree company needs modern website design

We need a website design for a tree company, here are some websites they like:

http://korvalemarine.com/company/ - we like the big image filling most of the page. Also the top half of the page looks good with the logo along top and good task bar also (we don’t like the spiel on left hand side covering up the picture + too many words!) If we could have our logo at lop like this along with our slogan which is 'Great Looking Trees that Grow Well'

http://www.pinecroftgardens.co.nz/ - we like the bottom half of this with the clean lines and welcome to part down bottom rather than the spiel to the left as on above site. Also like the moving leaves, any chance we could have birds such as a fantail, Tui and Bellbirds flying across the page and also some birdsong playing?

This is their existing website, that needs an updated design: http://tallfernwood.co.nz/

Industry/Entity Type

It Company

Font styles to use
Serif
Sans Serif

Requirements
Must have
• "Website by Pages Built Simple" located in bottom right hand side
Use images provided as background or banner images
Should not have
• Social Media icons

```html
<!DOCTYPE html>
<html lang="en">
<head>
<meta charset="utf-8">
<title>Tallfernwood Trees</title>
<link href="https://fonts.googleapis.com/css2?family=Open+Sans:wght@400;600;700;800&display=swap" rel="stylesheet">
<style>
:root{
  --teal:#0f8a80;
  --teal-dark:#0a6b63;
  --teal-deep:#075650;
  --lime:#8cc63f;
  --lime-dark:#6fa52a;
  --ink:#333;
  --muted:#777;
  --line:#d9d9d9;
  --paper:#fff;
  --mist:#f0f0f0;
}
*{box-sizing:border-box;margin:0;padding:0}
html,body{width:1200px;height:3396px;overflow:hidden}
body{position:relative;font-family:"Open Sans",Arial,sans-serif;color:var(--ink);background:var(--paper)}
.abs{position:absolute}

/* hero */
.hero{left:0;top:0;width:1200px;height:780px;background:linear-gradient(180deg,#cfe5d2 0%,#9cc879 22%,#4f8f2e 45%,#3d7a24 62%,#7fbf3a 74%,#a7d65a 100%)}
.brand{left:120px;top:52px;width:300px;height:92px;background:var(--paper);clip-path:polygon(0 0,100% 0,88% 100%,0 100%);box-shadow:0 2px 6px rgba(0,0,0,.3);display:flex;align-items:center;padding-left:26px;gap:12px}
.brand-mark{width:22px;height:22px;background:var(--lime)}
.brand-name{font-weight:800;font-size:25px;color:var(--teal-dark);letter-spacing:.5px}
.nav{left:396px;top:64px;width:684px;height:64px;background:var(--teal-dark);display:flex;align-items:center;justify-content:space-around;padding:0 20px}
.nav a{color:#fff;text-decoration:none;font-size:15px;font-weight:600;letter-spacing:.5px}
.slogan{left:260px;top:360px;width:800px;height:64px;background:rgba(20,40,25,.55);border-left:8px solid var(--lime);display:flex;align-items:center;padding-left:22px;font-size:36px;font-weight:700;color:var(--lime)}
.dots{left:564px;top:692px;width:72px;height:20px;background:rgba(0,0,0,.35);border-radius:10px;display:flex;align-items:center;justify-content:center;gap:8px}
.dots i{width:9px;height:9px;border-radius:50%;background:#fff;opacity:.6}
.dots i:first-child{opacity:1;background:var(--lime)}

/* welcome */
.section-title{width:1200px;left:0;text-align:center;font-size:18px;letter-spacing:1px;color:var(--ink)}
.welcome-title{left:148px;top:812px;font-size:18px;letter-spacing:1px}
.welcome-title b{color:var(--teal);font-weight:700}
.welcome-rule{left:148px;top:848px;width:904px;height:1px;background:var(--line)}
.video{left:148px;top:872px;width:440px;height:252px;background:linear-gradient(180deg,#9fb9c9 0%,#6f8f5a 55%,#4d6b3a 100%)}
.video-play{left:338px;top:970px}
.video-bar{left:148px;top:1102px;width:440px;height:22px;background:rgba(0,0,0,.7)}
.welcome-lead{left:620px;top:872px;width:430px;font-size:22px;line-height:30px;color:var(--ink)}
.welcome-lead em{font-style:normal;color:var(--teal);font-weight:600}
.welcome-body{left:620px;top:948px;width:430px;font-size:13.5px;line-height:21px;color:var(--muted)}
.btn-ghost{border:1px solid #bbb;background:#f7f7f7;font-size:13px;color:var(--muted);padding:6px 16px}
.welcome-more{left:620px;top:1140px}

/* projects */
.projects{left:0;top:1200px;width:1200px;height:700px;background:linear-gradient(180deg,#e6e6e6,#f6f6f6 30%,#ececec)}
.projects-title{top:1250px}
.title-rule{width:140px;height:1px;background:#aaa;left:530px}
.project-photo{width:224px;height:224px;border-radius:50%;border:6px solid #fff;box-shadow:0 3px 10px rgba(0,0,0,.25)}
.p1{left:180px;top:1360px;background:linear-gradient(160deg,#9cc0e0,#5b6f7e 60%,#3d4b3a)}
.p2{left:488px;top:1360px;background:linear-gradient(160deg,#7ea0c4,#6a8a55 55%,#7a5d44)}
.p3{left:800px;top:1360px;background:linear-gradient(160deg,#c7d8e8,#6d9b55 60%,#3f6c2e)}
.project-cap{width:300px;text-align:center;font-size:12px;line-height:18px;color:var(--muted)}
.project-cap b{display:block;color:var(--ink);font-size:12.5px;font-weight:700;text-transform:uppercase;margin-bottom:6px}
.btn-lime{background:var(--lime);color:#fff;font-size:13px;font-weight:600;padding:6px 18px;border-radius:2px}

/* news */
.news{left:0;top:1916px;width:1200px;height:456px;background:linear-gradient(180deg,var(--teal-dark),var(--teal) 50%,var(--teal-dark));border-top:6px solid var(--lime)}
.news-title{top:1966px;color:#fff}
.news-photo{width:280px;height:176px;border:4px solid #fff;background:linear-gradient(180deg,#8fb8de 0%,#c9dceb 45%,#7b8b75 70%,#5f7f3f 100%)}
.date{width:48px;height:54px;background:var(--lime);color:#fff;text-align:center;font-size:11px;line-height:14px;padding-top:6px}
.date b{display:block;font-size:20px;line-height:24px}
.news-head{width:280px;color:#fff;font-size:15px;font-weight:700;text-transform:uppercase}
.news-body{width:280px;color:#d7efec;font-size:12.5px;line-height:19px}
.btn-white{background:#fff;color:var(--teal-dark);font-size:12px;padding:5px 14px}

/* testimonials */
.testi-title{top:2420px}
.face{border-radius:50%;border:5px solid #fff;box-shadow:0 2px 8px rgba(0,0,0,.25);background:linear-gradient(180deg,#c9c9c9,#8a8a8a)}
.arrow{top:2560px}
.person{left:0;width:1200px;text-align:center}
.quote{left:300px;top:2740px;width:600px;height:170px;border:1px solid var(--line);background:#fafafa;padding:34px 60px;font-size:13px;line-height:21px;color:var(--muted);text-align:center}
.qmark{font-size:60px;color:#ccc;font-family:Georgia,serif;line-height:1}

/* footer */
.footer{left:0;top:2988px;width:1200px;height:352px;background:var(--teal);border-top:6px solid var(--lime)}
.foot-h{color:#fff;font-size:18px;font-weight:700}
.foot-list{list-style:none;color:#e0f3f1;font-size:13px;line-height:28px}
.foot-list li::before{content:"▸ ";color:var(--lime)}
.contact-row{color:#e0f3f1;font-size:13px;display:flex;align-items:center;gap:10px}
.circle-ico{width:22px;height:22px;border-radius:50%;background:#fff;display:inline-block}
.field{background:#fff;height:30px;font-size:11px;color:#999;padding:7px 8px}
.bottom{left:0;top:3340px;width:1200px;height:56px;background:var(--teal-deep);color:#bfe0dc;font-size:12px}
</style>
</head>
<body>

<!-- Hero -->
<div class="abs hero" role="img" aria-label="Photograph of a tree-lined avenue over a wide green lawn"></div>
<div class="abs brand"><span class="brand-mark"></span><span class="brand-name">TALLFERNWOOD</span></div>
<nav class="abs nav"><a>HOME</a><a>ABOUT US</a><a>TREE GALLERY</a><a>PROJECTS</a><a>CATALOGUE</a><a>CONTACT</a></nav>
<div class="abs slogan">Great Looking Trees that Grow Well.</div>
<div class="abs dots"><i></i><i></i><i></i><i></i></div>

<!-- Welcome -->
<h2 class="abs welcome-title">WELCOME TO <b>TALLFERNWOOD TREES</b></h2>
<div class="abs welcome-rule"></div>
<div class="abs video" role="img" aria-label="Video still of young trees planted along a driveway"></div>
<svg class="abs video-play" width="60" height="44" viewBox="0 0 60 44"><rect width="60" height="44" rx="8" fill="#222" opacity=".85"/><path d="M24 13 L40 22 L24 31 Z" fill="#fff"/></svg>
<div class="abs video-bar"></div>
<p class="abs welcome-lead">Do you need <em>semi mature trees</em><br>for <em>instant effect?</em></p>
<p class="abs welcome-body">Most are available for immediate delivery New Zealand wide. All trees are grown in 100% Southland peat, a natural soil medium. They grow better and are lighter and easier to transport. Your tree requirements can be in large numbers of even grades. We offer contract growing of trees in advance for future projects. You can trust Tallfernwood Trees to deliver the goods and exceed your expectations.</p>
<span class="abs btn-ghost welcome-more">Read More</span>

<!-- Projects -->
<div class="abs projects"></div>
<h2 class="abs section-title projects-title">RECENT PROJECTS</h2>
<div class="abs title-rule" style="top:1284px"></div>
<div class="abs project-photo p1" role="img" aria-label="Modern campus building with young street trees"></div>
<div class="abs project-photo p2" role="img" aria-label="Lakeside village homes screened by planted trees"></div>
<div class="abs project-photo p3" role="img" aria-label="Hillside community with established conifers"></div>
<p class="abs project-cap" style="left:142px;top:1608px"><b>Riverside Stadium &amp; Campus Building, City Centre</b>A prestigious project with wide and view edge architecture. This project included plantings of hardy trees.</p>
<p class="abs project-cap" style="left:450px;top:1608px"><b>Lakeside Village with Screening with Privacy &amp; Calm</b>Shoreline homes in the upper lake basin. Our trees provide excellent screening in the mountain environment.</p>
<p class="abs project-cap" style="left:762px;top:1608px"><b>Peaceful Tree Lined Community</b>A new well planned hillside development by residents with a selection of hardy street trees including the Totara.</p>
<span class="abs btn-lime" style="left:248px;top:1742px">View Project</span>
<span class="abs btn-lime" style="left:556px;top:1742px">View Project</span>
<span class="abs btn-lime" style="left:868px;top:1742px">View Project</span>

<!-- News -->
<div class="abs news"></div>
<h2 class="abs section-title news-title">NEWS ARTICLES</h2>
<div class="abs title-rule" style="top:2000px;background:#7fc3bc"></div>
<div class="abs news-photo" style="left:148px;top:2030px" role="img" aria-label="Building frontage with planted trees"></div>
<div class="abs news-photo" style="left:460px;top:2030px" role="img" aria-label="Building frontage with planted trees"></div>
<div class="abs news-photo" style="left:772px;top:2030px" role="img" aria-label="Building frontage with planted trees"></div>
<div class="abs date" style="left:160px;top:2040px">JUL<b>18</b></div>
<div class="abs date" style="left:472px;top:2040px">JUL<b>18</b></div>
<div class="abs date" style="left:784px;top:2040px">JUL<b>18</b></div>
<h3 class="abs news-head" style="left:148px;top:2222px">Title of the article goes here</h3>
<h3 class="abs news-head" style="left:460px;top:2222px">Title of the article goes here</h3>
<h3 class="abs news-head" style="left:772px;top:2222px">Title of the article goes here</h3>
<p class="abs news-body" style="left:148px;top:2248px">Lorem ipsum dolor sit amet, consectetur adipiscing elit. Phasellus tincidunt tellus leo, sodales vestibulum urna.</p>
<p class="abs news-body" style="left:460px;top:2248px">Lorem ipsum dolor sit amet, consectetur adipiscing elit. Phasellus tincidunt tellus leo, sodales vestibulum urna.</p>
<p class="abs news-body" style="left:772px;top:2248px">Lorem ipsum dolor sit amet, consectetur adipiscing elit. Phasellus tincidunt tellus leo, sodales vestibulum urna.</p>
<span class="abs btn-white" style="left:148px;top:2312px">Read more</span>
<span class="abs btn-white" style="left:460px;top:2312px">Read more</span>
<span class="abs btn-white" style="left:772px;top:2312px">Read more</span>

<!-- Testimonials -->
<h2 class="abs section-title testi-title">CLIENT TESTIMONIALS</h2>
<div class="abs title-rule" style="top:2454px"></div>
<svg class="abs arrow" style="left:180px" width="24" height="40" viewBox="0 0 24 40"><path d="M20 4 L4 20 L20 36" fill="none" stroke="#bbb" stroke-width="4"/></svg>
<svg class="abs arrow" style="left:996px" width="24" height="40" viewBox="0 0 24 40"><path d="M4 4 L20 20 L4 36" fill="none" stroke="var(--teal)" stroke-width="4"/></svg>
<div class="abs face" style="left:234px;top:2520px;width:96px;height:96px" role="img" aria-label="Client portrait"></div>
<div class="abs face" style="left:394px;top:2520px;width:96px;height:96px" role="img" aria-label="Client portrait"></div>
<div class="abs face" style="left:536px;top:2496px;width:128px;height:128px" role="img" aria-label="Client portrait"></div>
<div class="abs face" style="left:710px;top:2520px;width:96px;height:96px" role="img" aria-label="Client portrait"></div>
<div class="abs face" style="left:870px;top:2520px;width:96px;height:96px" role="img" aria-label="Client portrait"></div>
<p class="abs person" style="top:2640px;font-size:14px;font-weight:700">JANE DOE</p>
<p class="abs person" style="top:2662px;font-size:12px;color:var(--muted)">Job Position</p>
<div class="abs quote">Lorem ipsum dolor sit amet, consectetur adipiscing elit. Etiam dapibus, mauris ac aliquam elementum, felis erat porta elit, ut scelerisque ligula arcu vitae risus. Sed interdum odio a eros dictum, in dignissim augue dictum. Proin augue leo, venenatis sit amet, sodales tristique sapien.</div>
<span class="abs qmark" style="left:318px;top:2730px">&ldquo;</span>
<span class="abs qmark" style="left:852px;top:2858px">&rdquo;</span>

<!-- Footer -->
<div class="abs footer"></div>
<h3 class="abs foot-h" style="left:210px;top:3040px">Quicklinks</h3>
<ul class="abs foot-list" style="left:210px;top:3080px"><li>Link goes here</li><li>Link goes here</li><li>Link goes here</li><li>Link goes here</li></ul>
<ul class="abs foot-list" style="left:360px;top:3080px"><li>Link goes here</li><li>Link goes here</li><li>Link goes here</li><li>Link goes here</li></ul>
<h3 class="abs foot-h" style="left:552px;top:3040px">Contact us</h3>
<div class="abs contact-row" style="left:552px;top:3086px"><span class="circle-ico"></span>sales@tallfernwood.co.nz</div>
<div class="abs contact-row" style="left:552px;top:3122px"><span class="circle-ico"></span>0800 555 014</div>
<div class="abs" style="left:552px;top:3162px;display:flex;gap:8px"><span class="circle-ico"></span><span class="circle-ico"></span><span class="circle-ico"></span><span class="circle-ico"></span></div>
<h3 class="abs foot-h" style="left:796px;top:3040px">Quick Contact</h3>
<p class="abs" style="left:796px;top:3078px;width:260px;color:#e0f3f1;font-size:12px;line-height:17px">If you have any question, feel free to send us a message:</p>
<div class="abs field" style="left:796px;top:3122px;width:124px">Your name</div>
<div class="abs field" style="left:928px;top:3122px;width:124px">Email</div>
<div class="abs field" style="left:796px;top:3160px;width:256px;height:84px">Message</div>
<span class="abs btn-lime" style="left:796px;top:3260px">SUBMIT</span>
<div class="abs bottom"></div>
<p class="abs" style="left:210px;top:3360px;color:#bfe0dc;font-size:12px">Copyright © 2015 Tallfernwood Trees</p>
<p class="abs" style="left:860px;top:3360px;color:#bfe0dc;font-size:12px;word-spacing:14px">Help Sitemap Privacy&nbsp;Policy</p>

</body>
</html>
```